Wine Label Design-Crumbled Ledge Vineyard

Crumbled Ledge Vineyard is in the Barossa Valley in South Australia. The Barossa is recognized as Australia's premier wine region, producing Australia's icon wines and some " new takes on traditional".
This family owned and operated vineyard grows some exceptionally high quality fruit. Most of the fruit is sold and used for some of Australia's most iconic wines. Small quantities are retained by the owners for some wines with very limited availability. (Wines were previously sold as BrellMarston Vineyards Crumbled Ledge ( Shiraz, Cabernet etc).

The wines will in the future be labeled simply ‘Crumbled Ledge Vineyard’. The label will launch this new identity for the single family single vineyard and its high quality wines which are a true expression of the vineyard and derive from the Crumbled Ledge common to this ancient area (800-2000 million years old).
The label should reflect
• Single vineyard, family owned
• vines in very old rock & soils
• High quality & reliability
• Edgy but true, design based thinking (Please note:blue is generally seen as an unacceptable colour for a wine label?? Don’t ask me why)

The wines will be sold mostly direct in Australia ( ie not through retail stores), with limited export to Asia, Scandinavia and Canada.
There are three quality levels and price points in the portfolio
1. Entry level premium for everyday drinking for discriminating drinkers-approx AUD20
2. Super Premium-approx AUD30
3. Limited Release ultlra premium-AUD75-90?
We envisage three variations on the label but with an obvious & common design element. This design element should be able to be used for corporate identification and promotion
The paper stock will be waterproof and self adhesive. Our preference is for designs that engage the user by appealing to both sight and touch. It is preferred that textures be added eg embossing, high build varnish etc-rather than be a facet of the stock itself.
For information on statutory label requirements refer to www.vinoregistry-example.com . In brief
o Front label need not show any mandatory information. However we would prefer Variety, Barossa Valley, Year and alcohol to be shown on the front label
o Back label should show all mandatories and allow for a bar code

Reason: I've had a problem with my wireless broadband account and reception has been intermittent to say the least to the extent that I switched off at the weekend. Just going downtown now for a 'polite discussion' with my service provider.

Reason: I have receiver insufficient designs of quality which we would consider. Too many designs have a "cut and paste" appearance - too few exhibit an original art/design element which truly identifies the product.

Gals & Guys

most of the designs submitted lack punch and originality and are totally unmemorable.
Please-get on Zindle or whatever enter "Wine Label Designs" and do some research b4 u waste your time and mine. Formulaic cut and paste will not win the day. That's not to say that cut and paste can't work-but it must have some originality, impact and command attention. Please surprise me.

Following on from a question from a designer about who is our competition and what we are looking for I sent the following 
"I don't think I can add anything new. Read the brief and comments again and research wine labels on the web. In 30 minutes you'll get a good idea of the creative edgy designs in the industry. There are a plethora of collections. Our competition-anyone with a label. In 2010 there were over 2400 "producers" in other words 2400 producers with at least one label. In fact there are over 25000 Australian wines and then the numerous imported wines.

Target Market(s)

$20 people who budget everyday but have graduated from drinking 'entry level' wines. These people will likely fit into Cat. (b) in the $30 wine

$30 (a) will not over-compromise on some everyday discretionary expenditure.(b) might buy for special occasions

$70-$90 Professional/successful people with high disposable/discretionary income not particularly worried about recession. wine geeks.

Industry/Entity Type

Retail

Requirements
Must have
• identifiable element across range of wines

```html
<!DOCTYPE html>
<html lang="en">
<head>
<meta charset="utf-8">
<title>Crumbled Ledge Vineyard – Shiraz Label</title>
<link rel="stylesheet" href="https://fonts.googleapis.com/css2?family=Aladin&family=Pathway+Gothic+One&display=swap">
<style>
  :root {
    --ink: #000000;
    --paper: #ffffff;
    --gold: #ffff00;
    --red: #ff1c24;
    --flame: #ff4a1c;
    --edge: #f3e9b0;
    --script: "Aladin", cursive;
    --body: "Pathway Gothic One", sans-serif;
  }
  * { box-sizing: border-box; margin: 0; padding: 0; }
  html, body { width: 1089px; height: 1200px; overflow: hidden; background: var(--paper); }
  .canvas { position: relative; width: 1089px; height: 1200px; }

  .swatch { position: absolute; top: 34px; width: 72px; height: 67px; }
  .swatch--gold { left: 632px; background: var(--gold); }
  .swatch--red { left: 739px; background: var(--red); }
  .swatch--flame { left: 848px; background: var(--flame); }

  .front-label {
    position: absolute; left: 530px; top: 134px; width: 502px; height: 1052px;
    background: var(--ink); border: 2px solid var(--edge);
  }
  .front-label__emblem {
    position: absolute; left: 75px; top: 110px; width: 291px; height: 187px;
  }
  .rule { position: absolute; left: 0; width: 100%; height: 8px; background: var(--gold); }
  .rule--top { top: 340px; }
  .rule--bottom { top: 558px; }
  .name-band {
    position: absolute; left: 0; top: 358px; width: 100%; height: 190px;
    display: flex; flex-direction: column; justify-content: center; align-items: center;
    background: var(--gold); color: var(--ink); font-family: var(--script);
    font-weight: 400; text-align: center; font-size: 70px; line-height: 80px;
  }
  .name-band__line { display: block; }
  .front-label__details {
    position: absolute; left: 0; top: 775px; width: 100%; text-align: center;
    color: var(--gold); font-family: var(--script);
  }
  .front-label__region { font-size: 44px; line-height: 58px; }
  .front-label__variety { font-size: 44px; line-height: 58px; }
  .front-label__vintage { font-size: 34px; line-height: 60px; }

  .back-label {
    position: absolute; left: 62px; top: 488px; width: 402px; height: 698px;
    background: var(--ink); text-align: center;
  }
  .back-label__title {
    margin-top: 22px; color: var(--gold); font-family: var(--script);
    font-weight: 400; font-size: 31px; line-height: 42px;
  }
  .back-label__info {
    color: var(--paper); font-family: var(--body); font-size: 21px; line-height: 29px;
  }
  .back-label__info--legal { margin-top: 14px; }
  .back-label__info--producer { margin-top: 30px; }
  .back-label__barcode-space {
    position: absolute; left: 48px; top: 455px; width: 306px; height: 228px;
    background: var(--paper);
  }
</style>
</head>
<body>
<main class="canvas">
  <div class="swatch swatch--gold"></div>
  <div class="swatch swatch--red"></div>
  <div class="swatch swatch--flame"></div>

  <section class="back-label">
    <h2 class="back-label__title">Crumbled Ledge<br>Vineyard<br>2012 Shiraz</h2>
    <p class="back-label__info back-label__info--legal">13.5% ALC/VOL Approx. 8.3 Standard Drinks<br>Preservative (220) Added</p>
    <p class="back-label__info back-label__info--producer">Produced By: Crumbled Ledge Vineyards<br>Lot 1 Hollowbrook Ridge Road, Kelvara, SA 5999<br>Mobile:0000 000 000<br>Email: hello@crumbledledge-example.com<br>www.crumbledledge-example.com<br>750ml WINE OF AUSTRALIA</p>
    <div class="back-label__barcode-space"></div>
  </section>

  <section class="front-label">
    <svg class="front-label__emblem" role="img" aria-label="Illustration of a charging bull in dark green and yellow" viewBox="0 0 291 187">
      <defs>
        <linearGradient id="emblemTone" x1="0" y1="1" x2="1" y2="0">
          <stop offset="0" stop-color="#0d1a05"/>
          <stop offset="0.6" stop-color="#2f4a0a"/>
          <stop offset="1" stop-color="#a8b400"/>
        </linearGradient>
      </defs>
      <rect width="291" height="187" rx="14" fill="url(#emblemTone)"/>
    </svg>
    <div class="rule rule--top"></div>
    <h1 class="name-band">
      <span class="name-band__line">Crumbled Ledge</span>
      <span class="name-band__line">Vineyard</span>
    </h1>
    <div class="rule rule--bottom"></div>
    <div class="front-label__details">
      <p class="front-label__region">Barossa Valley</p>
      <p class="front-label__variety">Shiraz</p>
      <p class="front-label__vintage">2012</p>
    </div>
  </section>
</main>
</body>
</html>
```